Letterhead Design Project

Looking for letterhead designs for Brastova Mining.

I am looking for a letterhead design in conjunction with a business card design. I have opened contests for both but ask that if you submit a letterhead design you also submit a business card design with a corresponding look/feel.

Brastova Mining is a B2B company that buys and sells large machinery tires within the coal mining industry. The design should the strong, crisp and masculine. I have uploaded the company logo and mock-up of the back of the company's business card.

Color scheme should be grey/green/black

Contact information to include:
Name: Dale Whitford
Title: Managing Director
Phone: 555-231-4097
Address: 1817 Pellam #3 Dallas, TX 75290
Email: Dale@Brastova.example
Updates

Project Deadline Extended
Reason: Looking for a more refined, elegant letterhead than what's been submitted as of yet. Here is a sample of what we're looking for: http://www.plumcrestgallery.example/letterhead-designs/ We will also be increasing the payment.

Industry/Entity Type

Coal Mining

```html
<!DOCTYPE html>
<html lang="en">
<head>
<meta charset="utf-8">
<title>Brastova Mining – Letterhead &amp; Business Card</title>
<link href="https://fonts.googleapis.com/css2?family=Saira+Semi+Expanded:wght@400;600;700&family=Arimo:wght@400;700&display=swap" rel="stylesheet">
<style>
  :root {
    --green: #5fa514;
    --grey: #4a4c4e;
    --ink: #111111;
    --paper: #ffffff;
    --black: #050505;
    --backdrop: #ecebe8;
  }
  * { box-sizing: border-box; margin: 0; padding: 0; }
  html, body { width: 1199px; height: 1200px; overflow: hidden; }
  body { background: var(--backdrop); position: relative; font-family: "Saira Semi Expanded", sans-serif; color: var(--ink); }

  .brand { display: flex; align-items: center; gap: 8px; }
  .brand-square { width: 16px; height: 16px; background: var(--green); flex: none; }
  .brand-name { font-family: "Saira Semi Expanded", sans-serif; font-weight: 700; color: var(--grey); letter-spacing: 1px; white-space: nowrap; }

  /* Letterhead */
  .letterhead { position: absolute; left: 92px; top: 125px; width: 735px; height: 949px; background: var(--paper); box-shadow: 0 2px 6px rgba(0,0,0,.25); }
  .letterhead .brand { position: absolute; left: 52px; top: 58px; }
  .letterhead .brand-square { width: 30px; height: 30px; }
  .letterhead .brand-name { font-size: 24px; }
  .header-rule { position: absolute; left: 97px; right: 0; top: 102px; height: 3px; background: var(--green); }
  .salutation { position: absolute; left: 52px; top: 166px; font-size: 13px; font-weight: 700; }
  .letter-body { position: absolute; left: 52px; top: 206px; width: 622px; font-size: 10.4px; line-height: 14px; text-align: justify; }
  .letter-body p + p { margin-top: 14px; }
  .closing { position: absolute; left: 52px; top: 713px; font-size: 10.5px; line-height: 15px; }
  .closing strong { font-size: 13px; display: block; }
  .signature { position: absolute; left: 52px; top: 752px; width: 100px; height: 46px; background: linear-gradient(90deg, #e6effa, #cfe0f5); }
  .letter-footer { position: absolute; right: 26px; top: 840px; text-align: right; font-family: "Arimo", sans-serif; color: var(--grey); font-size: 16px; line-height: 21px; }
  .letter-footer .company { color: var(--green); font-weight: 700; font-size: 22px; line-height: 28px; margin-bottom: 2px; }
  .label { color: var(--green); }
  .footer-band { position: absolute; left: 0; right: 0; bottom: 0; height: 15px; background: var(--green); }

  /* Card front */
  .card { position: absolute; left: 854px; width: 306px; height: 168px; box-shadow: 0 2px 6px rgba(0,0,0,.3); }
  .card-front { top: 125px; background: var(--paper); font-family: "Arimo", sans-serif; }
  .card-front .marker { position: absolute; right: 0; top: 34px; width: 7px; height: 21px; background: var(--green); }
  .card-front .person { position: absolute; right: 13px; top: 34px; text-align: right; }
  .person .name { font-size: 10px; font-weight: 700; line-height: 12px; }
  .person .title { font-size: 7px; color: var(--grey); line-height: 10px; }
  .card-front .brand { position: absolute; left: 25px; top: 58px; gap: 5px; }
  .card-front .brand-square { width: 14px; height: 14px; }
  .card-front .brand-name { font-size: 12px; }
  .card-contact { position: absolute; right: 13px; top: 80px; text-align: right; font-size: 7px; line-height: 9.5px; color: var(--ink); }
  .card-contact .company { color: var(--green); font-size: 10.5px; line-height: 14px; }
  .card-contact .lines { margin-top: 10px; }
  .card-contact .label { font-weight: 700; }
  .card-band { position: absolute; left: 0; right: 0; bottom: 0; height: 6px; background: var(--green); }

  /* Card back */
  .card-back { top: 334px; background: var(--black); display: flex; align-items: center; justify-content: center; }
  .card-back .brand-square { width: 22px; height: 22px; }
  .card-back .brand-name { color: #ffffff; font-size: 20px; }
</style>
</head>
<body>

<section class="letterhead">
  <div class="brand"><span class="brand-square"></span><span class="brand-name">BRASTOVA MINING</span></div>
  <div class="header-rule"></div>

  <p class="salutation">Dear Sir/Madam</p>

  <div class="letter-body">
    <p>Peditemp oriorumquia qui aut laborep ereptur, sinum ium rectes re litiam, sam quibus, aut expe volupta tionsed et unties et idus, temolup tasperovid erovit officiis sus, solland enducius ipiciis ius abo. Or as nectota et landaes torestiis exerfero et volore omnimagnatem fugia eost re soluptae nam quo et, non perrum dent.<br>Aligendae id ut ommos ea sitem latem solupta quas sae iscia destem ut ea cume porererio corerit harum faccaboris demporetur?</p>
    <p>Namus magnis ipsum ipsam, untur sam quo doluptio. Nam reperum quaeprestem laut omn aepro et ex expernatin pa quis utempost il il incipsa pro quaecus secest et facero tem repeed modit, sust fuga. Nam, sit acesequo est quas enis voloresequam excestrum fugitatur, odia pliquis doluptia voles re pe modi res aut adi dolupti volo iures velia coreperem num similit vent, cusantion nimagnatus ut volecti dis et, conet expelique nihitia veriorem. Ent molenimus dolupta dit exerspe rciaspe liquibus quia non cus, ut hil ipsa quis ea volupis es re officium etur alitatu riteectae suntio. Nam, sequosa perumquam qui tem ullori aut quam nobitib ernature expe nes dit magnis exerspisit volorem velia-tus cone num ut optation poressum inti optus dipid que qui cus adi ipit odigento odionse quuntia corum eici non premporio ma quo ea nonsed et laut volupta tusapid moluptibero vellacepro voluptate laborrovid quae nonsequaesse venturist et pellore ssinciis aut minieni ducia debit, volore dolor am, soluptate quuntestiur sit, netur?</p>
    <p>Dae occat. Ipidus il ipidemo luptate cerspe nonsequo berspie ntiusan debisi natum nobit occumetus aritate molorec aborporum la volupti quis molupti orepude eatquiste ne dusdanis eum aut qui conse intem lab illupta. Olumquiat et el eaqui volo et et ea si quam a dolorunt eum ipsam, qui conse-quame dolo officil laborem quatuscil mos molest, ut a none labores eum dolut eici utatio mintibus endam quam nest assimo ex eos exerum non rem et voluptat aborum quodit quae dit ant harum dusdam, cust fugiaest am ent volor sae vollacipsum quis atist qui ducid experovid minimol oressun-tia iur, cus, alibus ipsae vent, cum exere plabore stiati aut que et haribusam volupti isquis ea pror audigendio mo tem eic torporest, que volorenest accus nim ullici accus.</p>
    <p>Etur, con eiuntur? Qui bea vendi con nis quid quo tet doles et od que nonsed quissiment lit prehend iaestiis autecte nonsed quo quae.</p>
  </div>

  <div class="closing">Yours Sincerley<strong>Name Name</strong></div>
  <div class="signature" role="img" aria-label="Handwritten signature"></div>

  <div class="letter-footer">
    <div class="company">Brastova Mining</div>
    <div>1817 Pellam #3 Dallas, TX 75290</div>
    <div><span class="label">Phone:</span> 555-231-4097, <span class="label">Web:</span> www.brastova.example</div>
  </div>
  <div class="footer-band"></div>
</section>

<section class="card card-front">
  <div class="marker"></div>
  <div class="person">
    <div class="name">Dale Whitford</div>
    <div class="title">Managing Director</div>
  </div>
  <div class="brand"><span class="brand-square"></span><span class="brand-name">BRASTOVA MINING</span></div>
  <div class="card-contact">
    <div class="company">Brastova Mining</div>
    <div>1817 Pellam #3 Dallas</div>
    <div>TX 75290</div>
    <div class="lines">
      <div><span class="label">Phone:</span> 555-231-4097</div>
      <div><span class="label">Email:</span> Dale@Brastova.example</div>
      <div><span class="label">Web:</span> www.brastova.example</div>
    </div>
  </div>
  <div class="card-band"></div>
</section>

<section class="card card-back">
  <div class="brand"><span class="brand-square"></span><span class="brand-name">BRASTOVA MINING</span></div>
</section>

</body>
</html>
```